Zielgruppe
Endkunde ist eine Immobilienfirma ((Bauträger)
Aufgabenstellung
Das Design soll für eine Präsentationsmappe erstellt werden und die Bemaßung sowie Farbigleit der vorgegebnen pdf-Datei beinhalten. Es soll in den Hausfarben , nebst den Backround in grau, gehalten werden.

```html
<!DOCTYPE html>
<html lang="de">
<head>
<meta charset="utf-8">
<title>Präsentationsmappe – Wohnwert Elbland AG</title>
<link href="https://fonts.googleapis.com/css2?family=Montserrat:wght@400;500&display=swap" rel="stylesheet">
<style>
  :root{
    --paper:#ffffff;
    --folder-grey:#c6c6c6;
    --band-dark:#5f5f5f;
    --brand-red:#8f2a22;
    --text-grey:#4a4a4a;
    --cut-line:#e879b8;
    --fold-line:#39b4e6;
    --photo-light:#eceded;
    --photo-mid:#b9bbbd;
  }
  *{margin:0;padding:0;box-sizing:border-box}
  html,body{width:1200px;height:883px;overflow:hidden;background:var(--paper)}
  body{font-family:"Montserrat",Arial,sans-serif;position:relative}
  .dieline{position:absolute;left:0;top:0}
  .txt{position:absolute;white-space:nowrap;color:var(--text-grey)}
  .slogan{top:275px;font-size:12.5px;color:#fff;transform:translateX(-50%)}
  .brand-name{color:var(--brand-red);font-weight:500}
  .inner-brand{right:778px;top:141px;font-size:14px;text-align:right}
  .cover-brand{right:212px;top:160px;font-size:27px;text-align:right;line-height:1.25}
  .contact{font-size:10px;transform:translateX(-50%)}
  .contact-rule{position:absolute;left:232px;top:198px;width:323px;height:1px;background:var(--text-grey)}
  .cover-web{left:935px;top:691px;font-size:12.5px;color:#fff;transform:translateX(-50%)}
  .flap-upside{position:absolute;left:272px;top:774px;width:312px;height:56px;transform:rotate(180deg);text-align:center}
  .flap-upside .brand-name{display:block;font-size:11px}
  .flap-upside .rule{height:1px;background:#e8e8e8;margin:10px 0 6px}
  .flap-upside .flap-contact{display:block;font-size:8px;color:#fff;white-space:nowrap}
</style>
</head>
<body>

<svg class="dieline" width="1200" height="883" viewBox="0 0 1200 883">
  <defs>
    <linearGradient id="photoTone" x1="0" y1="0" x2="1" y2="0">
      <stop offset="0" stop-color="var(--photo-mid)"/>
      <stop offset="0.45" stop-color="var(--photo-light)"/>
      <stop offset="1" stop-color="var(--photo-mid)"/>
    </linearGradient>
  </defs>

  <!-- left glue flap -->
  <path d="M138 13 L34 34 Q11 40 11 60 L11 680 Q11 700 34 705 L138 728 Z" fill="var(--folder-grey)"/>
  <rect x="11" y="105" width="127" height="143" fill="var(--paper)"/>
  <rect x="11" y="248" width="127" height="14" fill="var(--band-dark)"/>

  <!-- inner and cover panels -->
  <rect x="138" y="13" width="1048" height="717" fill="var(--folder-grey)"/>
  <rect x="138" y="105" width="1048" height="143" fill="var(--paper)"/>
  <rect x="138" y="248" width="1048" height="14" fill="var(--band-dark)"/>
  <rect x="150" y="374" width="1036" height="297" fill="url(#photoTone)" role="img" aria-label="Foto: Bauzeichnungen mit Zirkel und gerollten Bauplänen"/>

  <!-- bottom pocket flap -->
  <path d="M150 730 L660 730 L660 742 L634 870 L277 870 L252 845 Q240 860 220 858 Q185 852 172 825 Q166 800 185 785 Q175 770 181 760 L150 742 Z" fill="var(--folder-grey)"/>

  <!-- fold lines -->
  <g stroke="var(--fold-line)" stroke-width="0.8" fill="none">
    <line x1="150" y1="13" x2="150" y2="730"/>
    <line x1="662" y1="13" x2="662" y2="730"/>
    <line x1="675" y1="13" x2="675" y2="730"/>
    <line x1="150" y1="730" x2="660" y2="730"/>
    <line x1="150" y1="742" x2="660" y2="742"/>
  </g>
  <line x1="138" y1="13" x2="138" y2="728" stroke="#9a9a9a" stroke-width="0.8"/>

  <!-- cut lines -->
  <g stroke="var(--cut-line)" stroke-width="0.8" fill="none" stroke-dasharray="3 2">
    <path d="M138 13 L34 34 Q11 40 11 60 L11 680 Q11 700 34 705 L138 728"/>
    <path d="M138 13 L1186 13 L1186 730 L660 730"/>
    <path d="M660 742 L634 870 L277 870 L252 845 Q240 860 220 858 Q185 852 172 825 Q166 800 185 785 Q175 770 181 760 L150 742"/>
  </g>
  <g stroke="var(--cut-line)" stroke-width="0.9" fill="none">
    <path d="M40 623 L40 633 L100 693 L111 693"/>
    <path d="M480 752 Q492 772 505 752"/>
    <path d="M612 795 Q592 807 612 819"/>
  </g>

  <!-- brand squares -->
  <rect x="53" y="160" width="40" height="40" fill="var(--brand-red)"/>
  <rect x="428" y="140" width="16" height="16" fill="var(--brand-red)"/>
  <rect x="1002" y="166" width="46" height="46" fill="var(--brand-red)"/>
</svg>

<!-- inner panel -->
<div class="txt brand-name inner-brand">Wohnwert Elbland AG</div>
<div class="txt contact" style="left:392px;top:185px">Lindenhofweg 12 | 01468 Moritzgrund | Fon: 0351/40 18 27 50</div>
<div class="contact-rule"></div>
<div class="txt contact" style="left:392px;top:199px">Auenstraße 7 89561 | Talbrunnen | Fon 07324 /55 20 18</div>
<div class="txt contact" style="left:392px;top:227px">E-mail: kontakt@wohnwert-elbland.de | Web: www.wohnwert-elbland.de</div>
<div class="txt slogan" style="left:406px">IHRE ZUFRIEDENHEIT, IST UNSERE MOTIVATION!</div>

<!-- cover panel -->
<div class="txt brand-name cover-brand">Wohnwert<br>Elbland AG</div>
<div class="txt slogan" style="left:933px">IHRE ZUFRIEDENHEIT, IST UNSERE MOTIVATION!</div>
<div class="txt cover-web">E-mail: kontakt@wohnwert-elbland.de | Web: www.wohnwert-elbland.de</div>

<!-- pocket flap, printed upside down -->
<div class="flap-upside">
  <span class="brand-name">Wohnwert Elbland AG</span>
  <div class="rule"></div>
  <span class="flap-contact">E-mail: kontakt@wohnwert-elbland.de | Web: www.wohnwert-elbland.de</span>
</div>

</body>
</html>
```